Banner Design for High End Jewelry Website

We need a banner for our website (brivela.com) for a sale that we will be running. The banner should be a size 1187 × 400. I have included a few pieces of jewelry to be included in the banner (do not need to use all, can use just some). The banner should say:
"Christmas is Closer Than You Think Sale!"
Shop Now

Industry/Entity Type

Jewelry

```html
<!DOCTYPE html>
<html lang="en">
<head>
<meta charset="utf-8">
<title>Brivela — Fine Estate and Designer Jewelry</title>
<link href="https://fonts.googleapis.com/css2?family=Cabin:wght@400;500&family=Parisienne&display=swap" rel="stylesheet">
<style>
  :root {
    --brown: #a08471;
    --brown-dark: #7d6554;
    --ink: #4a4a4a;
    --muted: #7a7a7a;
    --band: #d8c6b8;
    --banner-light: #f7ece5;
    --banner-mid: #e9d7cb;
    --script: #a88a73;
    --line: #e2e2e2;
    --white: #ffffff;
  }
  * { box-sizing: border-box; margin: 0; padding: 0; }
  html, body { width: 1200px; height: 1031px; overflow: hidden; background: var(--white); }
  body { font-family: "Cabin", "Trebuchet MS", sans-serif; color: var(--ink); position: relative; }

  .utility { position: absolute; top: 14px; left: 0; width: 1200px; height: 24px; font-size: 15px; color: var(--muted); letter-spacing: 1px; }
  .utility span { position: absolute; display: flex; align-items: center; gap: 10px; }
  .utility .phone { left: 582px; }
  .utility .sell { left: 800px; }
  .utility .account { left: 996px; font-size: 13px; }

  .brand { position: absolute; left: 42px; top: 56px; width: 372px; }
  .brand-name { font-size: 84px; font-weight: 400; color: #222; letter-spacing: 2px; line-height: 1; }
  .brand-tagline { margin-top: 22px; font-size: 20px; color: #333; letter-spacing: 0.6px; white-space: nowrap; }

  .search { position: absolute; left: 530px; top: 74px; width: 320px; height: 30px; border-bottom: 1px solid #999; display: flex; align-items: center; }
  .search-label { margin-left: 48px; font-size: 12px; color: var(--muted); }
  .search-icon { position: absolute; left: 10px; top: 6px; }
  .search-go { position: absolute; right: 0; top: -1px; width: 31px; height: 31px; background: var(--brown-dark); display: flex; align-items: center; justify-content: center; }

  .shortcuts { position: absolute; top: 60px; left: 890px; display: flex; gap: 36px; }
  .shortcut { display: flex; flex-direction: column; align-items: center; gap: 8px; font-size: 13px; color: var(--muted); letter-spacing: 1px; }

  .main-nav { position: absolute; left: 437px; top: 137px; width: 731px; height: 46px; display: flex; background: var(--brown); }
  .main-nav a { flex: none; height: 46px; display: flex; align-items: center; justify-content: center; color: var(--white); text-decoration: none; font-size: 19px; letter-spacing: 1.2px; border-right: 2px solid var(--white); white-space: nowrap; }
  .main-nav a:last-child { border-right: none; }

  .sale-banner { position: absolute; left: 32px; top: 236px; width: 1143px; height: 386px; background: radial-gradient(ellipse at 45% 45%, var(--banner-light) 0%, var(--banner-mid) 75%, #e0ccbf 100%); border: 1px solid #eee; overflow: hidden; }
  .sale-headline { position: absolute; left: 72px; top: 86px; font-family: "Parisienne", cursive; font-weight: 400; color: var(--script); line-height: 1; white-space: nowrap; }
  .sale-headline .line1 { display: block; font-size: 78px; }
  .sale-headline .line2 { display: block; font-size: 64px; margin: 4px 0 0 146px; }
  .shop-now { position: absolute; left: 220px; top: 276px; width: 150px; height: 42px; border: 1px solid var(--brown-dark); color: var(--brown-dark); font-size: 16px; letter-spacing: 2px; display: flex; align-items: center; justify-content: center; text-decoration: none; }
  .sale-jewelry { position: absolute; left: 690px; top: 0; width: 453px; height: 386px; background: radial-gradient(closest-side circle at 38% 52%, #b9955a 0%, #9d8a72 30%, rgba(220,205,195,0.6) 65%, rgba(233,215,203,0) 100%); }

  .new-arrivals { position: absolute; left: 37px; top: 661px; width: 1131px; height: 380px; border: 1px solid var(--line); }
  .arrivals-header { height: 64px; background: var(--band); position: relative; display: flex; align-items: center; justify-content: center; }
  .arrivals-header h2 { font-weight: 400; font-size: 29px; color: var(--white); letter-spacing: 1px; }
  .view-all { position: absolute; right: 10px; top: 11px; width: 91px; height: 39px; background: var(--brown-dark); color: var(--white); font-size: 15px; letter-spacing: 1px; display: flex; align-items: center; justify-content: center; }

  .product { position: absolute; top: 82px; width: 340px; text-align: center; }
  .product-title { font-size: 12.5px; color: #333; line-height: 1.35; height: 40px; padding: 0 6px; }
  .product-photo { margin: 10px auto 0; width: 300px; height: 250px; background: radial-gradient(closest-side circle, #e7dcd2 0%, #ffffff 100%); }
  .product.p1 { left: 38px; }
  .product.p2 { left: 394px; }
  .product.p3 { left: 754px; }

  .carousel-arrow { position: absolute; top: 205px; width: 22px; height: 48px; background: #d9d1ca; display: flex; align-items: center; justify-content: center; }
  .carousel-arrow.prev { left: -1px; }
  .carousel-arrow.next { right: -1px; }
</style>
</head>
<body>

<div class="utility">
  <span class="phone">
    <svg width="18" height="18" viewBox="0 0 24 24" fill="none" stroke="#888" stroke-width="1.6"><path d="M5 3h4l2 5-3 2a12 12 0 0 0 6 6l2-3 5 2v4a2 2 0 0 1-2 2A18 18 0 0 1 3 5a2 2 0 0 1 2-2z"/></svg>
    800 - 555 - 0147
  </span>
  <span class="sell">
    <svg width="18" height="16" viewBox="0 0 24 20" fill="none" stroke="#888" stroke-width="1.6"><path d="M6 2h12l4 6-10 11L2 8z M2 8h20 M9 2l3 17 3-17"/></svg>
    SELL JEWELRY
  </span>
  <span class="account">
    <svg width="16" height="18" viewBox="0 0 20 22" fill="none" stroke="#888" stroke-width="1.6"><circle cx="10" cy="7" r="5"/><path d="M1 21c1-5 5-7 9-7s8 2 9 7"/></svg>
    SIGN IN / REGISTER
  </span>
</div>

<header class="brand">
  <div class="brand-name">Brivela</div>
  <div class="brand-tagline">FINE ESTATE AND DESIGNER JEWELRY</div>
</header>

<div class="search">
  <svg class="search-icon" width="16" height="16" viewBox="0 0 20 20" fill="none" stroke="#999" stroke-width="1.6"><circle cx="8" cy="8" r="6"/><path d="M13 13l5 5"/></svg>
  <span class="search-label">Search</span>
  <div class="search-go">
    <svg width="16" height="14" viewBox="0 0 16 14" fill="none" stroke="#fff" stroke-width="2.4"><path d="M2 7l4 4 8-9"/></svg>
  </div>
</div>

<nav class="shortcuts">
  <div class="shortcut">
    <svg width="24" height="18" viewBox="0 0 24 18" fill="none" stroke="#999" stroke-width="1.4"><rect x="1" y="1" width="22" height="16"/><path d="M1 1l11 9 11-9"/></svg>
    NEWSLETTER
  </div>
  <div class="shortcut">
    <svg width="24" height="20" viewBox="0 0 24 22" fill="none" stroke="#999" stroke-width="1.4"><path d="M12 21S1 14 1 7a5.5 5.5 0 0 1 11-1 5.5 5.5 0 0 1 11 1c0 7-11 14-11 14z"/></svg>
    WISHLIST
  </div>
  <div class="shortcut">
    <svg width="24" height="20" viewBox="0 0 24 22" fill="none" stroke="#999" stroke-width="1.4"><path d="M1 2h4l3 12h12l3-9H7"/><circle cx="10" cy="19" r="1.6"/><circle cx="18" cy="19" r="1.6"/></svg>
    CART (0)
  </div>
</nav>

<nav class="main-nav">
  <a style="width:170px">FINE JEWELRY</a>
  <a style="width:152px">TIMEPIECES</a>
  <a style="width:170px">ACCESSORIES</a>
  <a style="width:148px">DESIGNERS</a>
  <a style="width:91px">SALE</a>
</nav>

<section class="sale-banner">
  <h1 class="sale-headline">
    <span class="line1">Christmas is closer</span>
    <span class="line2">than you think sale!</span>
  </h1>
  <a class="shop-now">SHOP NOW</a>
  <div class="sale-jewelry" role="img" aria-label="Gold and diamond flower brooch with a pink cabochon centre, hanging silver Christmas baubles and curled ribbons"></div>
</section>

<section class="new-arrivals">
  <div class="arrivals-header">
    <h2>NEW ARRIVALS</h2>
    <div class="view-all">VIEW ALL</div>
  </div>

  <div class="carousel-arrow prev">
    <svg width="10" height="16" viewBox="0 0 10 16" fill="none" stroke="#fff" stroke-width="2.4"><path d="M8 2L2 8l6 6"/></svg>
  </div>

  <article class="product p1">
    <div class="product-title">Lunessa 6.00 Carat Fancy Diamond 18k Gold Bangle Bracelet</div>
    <div class="product-photo" role="img" aria-label="Wavy gold bangle bracelet set with fancy brown diamonds"></div>
  </article>
  <article class="product p2">
    <div class="product-title">Velmora Coil Diamond Tourmaline 18 Karat Rose Gold Ring</div>
    <div class="product-photo" role="img" aria-label="Coiled rose gold diamond ring with a triangular orange tourmaline"></div>
  </article>
  <article class="product p3">
    <div class="product-title">Art Deco Carved Emerald Ruby Diamond Platinum Brooch</div>
    <div class="product-photo" role="img" aria-label="Art Deco platinum brooch with carved emerald and ruby flower basket"></div>
  </article>

  <div class="carousel-arrow next">
    <svg width="10" height="16" viewBox="0 0 10 16" fill="none" stroke="#fff" stroke-width="2.4"><path d="M2 2l6 6-6 6"/></svg>
  </div>
</section>

</body>
</html>
```